Interactive Report Dashboard for Data Analytics

Please see this google doc for information and pictures regarding our project.
https://files.brindlework.net/sheet/d/7XpRmTqWz48NvKdLsEj2HbYf90GcAuUo3iZeMkPn/view?share=open
Feel free to message me if you have any questions.
Target Market(s)
This is for video producers, youtubers, and online teachers.
We run focus groups for them and help them understand how their audience reacts to the video content.
Coding
Coded - Design and coding required
Number of Pages Required
5+ page
Colors
Designer to choose colors to be used in the design.
Look and feel
Each slider illustrates characteristics of the customer's brand and the style your logo design should communicate.

```html
<!DOCTYPE html>
<html lang="en">
<head>
<meta charset="utf-8">
<title>Reactly – Audience Analytic Tools</title>
<link rel="stylesheet" href="https://fonts.googleapis.com/css2?family=Poppins:wght@400;500;600&family=Arimo:wght@400;700&display=swap">
<style>
:root{
  --navy:#0b1257;
  --orange:#f0550f;
  --text:#333;
  --muted:#555;
  --line:#dcdcdc;
  --panel:#fff;
  --blue:#2f46c8;
  --red:#d62b1a;
  --amber:#f7920f;
  --green:#15901a;
  --purple:#8a058f;
}
*{box-sizing:border-box;margin:0;padding:0}
html,body{width:1002px;height:1200px;overflow:hidden;background:#fff;font-family:Arimo,Arial,sans-serif;color:var(--text)}
.app{position:relative;width:1002px;height:1200px}
.topbar{position:absolute;left:0;top:0;width:1002px;height:56px;background:var(--navy);color:#fff}
.brand{position:absolute;left:8px;top:11px;font:500 25px Poppins,sans-serif}
.top-actions{position:absolute;right:10px;top:18px;display:flex;align-items:center;gap:11px;font:400 11px Poppins,sans-serif}
.toolbar{position:absolute;left:0;top:56px;width:1002px;height:40px;border-bottom:1px solid var(--line);font-size:9px}
.selected{position:absolute;left:8px;top:15px;color:#444}
.sort{position:absolute;left:715px;top:15px;color:#555}
.sort-select{position:absolute;left:754px;top:8px;width:177px;height:25px;border:1px solid var(--line);padding:7px 8px;font-size:9px;color:#444}
.sort-select svg{position:absolute;right:8px;top:9px}
.view-btn{position:absolute;top:8px;width:28px;height:25px;border:1px solid var(--line)}
.view-grid{left:936px;background:var(--orange);border-color:var(--orange)}
.view-list{left:964px}
.view-btn svg{position:absolute;left:9px;top:8px}
.sidebar{position:absolute;left:0;top:96px;width:185px;height:1054px;border-right:1px solid var(--line)}
.search{position:absolute;left:8px;top:24px;width:168px;height:26px;border:1px solid var(--line);background:#f3f3f3;font-size:9px;color:#666;padding:8px}
.search svg{position:absolute;right:8px;top:8px}
.f-label{position:absolute;left:8px;font-size:9px;color:#444}
.range-vals{position:absolute;left:8px;width:168px;font-size:9px;display:flex;justify-content:space-between;color:#555}
.range-vals .lo{color:var(--orange)}
.track{position:absolute;left:8px;width:168px;height:4px;border-radius:2px;background:#c9c9c9}
.track .fill{position:absolute;left:0;top:0;width:64px;height:4px;border-radius:2px;background:var(--orange)}
.track .knob{position:absolute;left:59px;top:-4px;width:11px;height:11px;border-radius:50%;background:#fff;border:3px solid var(--orange)}
.f-select{position:absolute;left:8px;width:168px;height:26px;border:1px solid var(--line);background:#f3f3f3}
.f-select svg{position:absolute;right:9px;top:9px}
.tabs{position:absolute;left:202px;top:115px;display:flex;gap:7px}
.tab{height:33px;border-radius:3px;background:var(--navy);color:#fff;font:500 10.5px Poppins,sans-serif;letter-spacing:.2px;display:flex;align-items:center;justify-content:center}
.tab.active{background:var(--orange)}
.cards{position:absolute;left:202px;top:184px;display:grid;grid-template-columns:repeat(3,252px);grid-auto-rows:292px;column-gap:14px;row-gap:18px}
.card{border:1px solid var(--line);background:var(--panel);padding:6px;text-align:center}
.chart{height:183px;border:1px solid #ececec}
.chart svg{display:block;width:100%;height:100%}
.card h3{margin-top:22px;font:500 11.5px Poppins,sans-serif;letter-spacing:.4px;color:#222}
.card p{margin-top:9px;font-size:9px;line-height:18.5px;color:#444;padding:0 8px}
.map-fill{width:100%;height:100%;background:radial-gradient(circle at 72% 35%,#2f8f2a 0 18%,transparent 30%),radial-gradient(circle at 28% 35%,#6bb35e 0 14%,transparent 26%),linear-gradient(#f5f5f5,#f5f5f5)}
.footer{position:absolute;left:0;top:1150px;width:1002px;height:50px;background:var(--navy);color:#fff;font:400 9.5px Poppins,sans-serif;text-align:center;line-height:50px}
.t{font-family:Arimo,Arial,sans-serif}
</style>
</head>
<body>
<div class="app">
  <header class="topbar">
    <div class="brand">Reactly</div>
    <div class="top-actions">
      <svg width="12" height="13" viewBox="0 0 12 13"><path d="M6 0c.6 0 1 .4 1 1v.3A4 4 0 0 1 10 5v3l1.5 2H.5L2 8V5a4 4 0 0 1 3-3.7V1c0-.6.4-1 1-1zM4.5 11h3a1.5 1.5 0 0 1-3 0z" fill="#fff"/></svg>
      <svg width="13" height="12" viewBox="0 0 24 23"><path d="M12 0l3.6 7.4 8.2 1.2-5.9 5.7 1.4 8.1L12 18.6l-7.3 3.8 1.4-8.1L.2 8.6l8.2-1.2z" fill="#fff"/></svg>
      <svg width="12" height="12" viewBox="0 0 12 12"><circle cx="6" cy="6" r="6" fill="#fff"/><rect x="5.2" y="5" width="1.6" height="4.5" fill="#0b1257"/><circle cx="6" cy="3.3" r=".9" fill="#0b1257"/></svg>
      <span>User</span>
      <svg width="8" height="5" viewBox="0 0 8 5"><path d="M0 0h8L4 5z" fill="#fff"/></svg>
    </div>
  </header>

  <div class="toolbar">
    <div class="selected"><svg width="7" height="5" viewBox="0 0 8 5"><path d="M0 0h8L4 5z" fill="#555"/></svg>&nbsp;&nbsp;0 Selected</div>
    <div class="sort">Sort by :</div>
    <div class="sort-select">Views : All (Most -Least )<svg width="14" height="6" viewBox="0 0 14 6"><rect x="0" y="0" width="1" height="6" fill="#aaa"/><path d="M6 1h7L9.5 5z" fill="#555"/></svg></div>
    <div class="view-btn view-grid"><svg width="10" height="9" viewBox="0 0 10 9" fill="#fff"><rect width="2.5" height="2"/><rect x="3.7" width="2.5" height="2"/><rect x="7.4" width="2.5" height="2"/><rect y="3.5" width="2.5" height="2"/><rect x="3.7" y="3.5" width="2.5" height="2"/><rect x="7.4" y="3.5" width="2.5" height="2"/><rect y="7" width="2.5" height="2"/><rect x="3.7" y="7" width="2.5" height="2"/><rect x="7.4" y="7" width="2.5" height="2"/></svg></div>
    <div class="view-btn view-list"><svg width="10" height="8" viewBox="0 0 10 8" fill="#555"><rect width="10" height="1.4"/><rect y="3.3" width="10" height="1.4"/><rect y="6.6" width="10" height="1.4"/></svg></div>
  </div>

  <aside class="sidebar">
    <div class="search">Search<svg width="9" height="9" viewBox="0 0 9 9"><circle cx="3.7" cy="3.7" r="2.9" fill="none" stroke="#555" stroke-width="1.4"/><path d="M5.8 5.8 8.5 8.5" stroke="#555" stroke-width="1.5"/></svg></div>
    <div class="f-label" style="top:64px">Age</div>
    <div class="range-vals" style="top:84px"><span class="lo">15.0</span><span>64.0</span></div>
    <div class="track" style="top:97px"><div class="fill"></div><div class="knob"></div></div>
    <div class="f-label" style="top:117px">Income</div>
    <div class="range-vals" style="top:137px"><span class="lo">11,067.0</span><span>119,615.0</span></div>
    <div class="track" style="top:150px"><div class="fill"></div><div class="knob"></div></div>
    <div class="f-label" style="top:183px">Nationality</div>
    <div class="f-select" style="top:198px"><svg width="14" height="6" viewBox="0 0 14 6"><rect width="1" height="6" fill="#aaa"/><path d="M6 1h7L9.5 5z" fill="#555"/></svg></div>
    <div class="f-label" style="top:237px">Education</div>
    <div class="f-select" style="top:252px"><svg width="14" height="6" viewBox="0 0 14 6"><rect width="1" height="6" fill="#aaa"/><path d="M6 1h7L9.5 5z" fill="#555"/></svg></div>
    <div class="f-label" style="top:290px">Gender</div>
    <div class="f-select" style="top:305px"><svg width="14" height="6" viewBox="0 0 14 6"><rect width="1" height="6" fill="#aaa"/><path d="M6 1h7L9.5 5z" fill="#555"/></svg></div>
    <div class="f-label" style="top:345px">Interests</div>
    <div class="f-select" style="top:360px"><svg width="14" height="6" viewBox="0 0 14 6"><rect width="1" height="6" fill="#aaa"/><path d="M6 1h7L9.5 5z" fill="#555"/></svg></div>
    <div class="f-label" style="top:400px">Personality</div>
    <div class="f-select" style="top:415px"><svg width="14" height="6" viewBox="0 0 14 6"><rect width="1" height="6" fill="#aaa"/><path d="M6 1h7L9.5 5z" fill="#555"/></svg></div>
  </aside>

  <nav class="tabs">
    <div class="tab active" style="width:168px">AUDIENCE ANALYTIC TOOLS</div>
    <div class="tab" style="width:168px">REAL TIME EMOTION DISPLAY</div>
    <div class="tab" style="width:168px">SURVEY RESPONSES</div>
  </nav>

  <main class="cards">
    <article class="card">
      <div class="chart"><div class="map-fill" role="img" aria-label="World map shaded green by audience count per country"></div></div>
      <h3>VISUALIZATION: GEOCHART</h3>
      <p>Sed ut perspiciatis unde omnis iste natus error sit volup architecto beatae vitae dicta sunt explicabo.</p>
    </article>

    <article class="card">
      <div class="chart"><svg viewBox="0 0 240 182">
        <text x="28" y="30" font-size="5" font-weight="700" class="t">Age vs. Weight comparison</text>
        <g stroke="#ddd" stroke-width=".6">
          <line x1="30" y1="40" x2="225" y2="40"/><line x1="30" y1="66" x2="225" y2="66"/><line x1="30" y1="92" x2="225" y2="92"/><line x1="30" y1="118" x2="225" y2="118"/>
          <line x1="79" y1="40" x2="79" y2="144"/><line x1="127" y1="40" x2="127" y2="144"/><line x1="176" y1="40" x2="176" y2="144"/><line x1="225" y1="40" x2="225" y2="144"/>
        </g>
        <line x1="30" y1="144" x2="225" y2="144" stroke="#333" stroke-width=".6"/><line x1="30" y1="40" x2="30" y2="144" stroke="#333" stroke-width=".6"/>
        <g font-size="4.5" class="t" fill="#444"><text x="22" y="42">20</text><text x="22" y="68">15</text><text x="22" y="94">10</text><text x="24" y="120">5</text><text x="24" y="146">0</text>
        <text x="29" y="152">0</text><text x="77" y="152">5</text><text x="124" y="152">10</text><text x="173" y="152">15</text><text x="222" y="152">20</text>
        <text x="121" y="166" font-style="italic">Age</text></g>
        <g fill="var(--blue)"><circle cx="60" cy="126" r="1.4"/><circle cx="69" cy="120" r="1.4"/><circle cx="69" cy="118" r="1.4"/><circle cx="94" cy="108" r="1.4"/><circle cx="108" cy="82" r="1.4"/><circle cx="137" cy="71" r="1.4"/></g>
      </svg></div>
      <h3>VISUALIZATION: SCATTER CHART</h3>
      <p>Sed ut perspiciatis unde omnis iste natus error sit volup architecto beatae vitae dicta sunt explicabo.</p>
    </article>

    <article class="card">
      <div class="chart"><svg viewBox="0 0 240 182">
        <text x="20" y="26" font-size="5" font-weight="700" class="t">Lengths of dinosaurs, in meters</text>
        <g fill="var(--blue)"><rect x="20" y="60" width="41" height="89"/><rect x="61" y="126" width="41" height="23"/><rect x="102" y="131" width="41" height="18"/><rect x="143" y="126" width="41" height="23"/><rect x="184" y="143" width="41" height="6"/></g>
        <g stroke="#fff" stroke-width=".5"><line x1="20" y1="66" x2="225" y2="66"/><line x1="20" y1="72" x2="225" y2="72"/><line x1="20" y1="78" x2="225" y2="78"/><line x1="20" y1="84" x2="225" y2="84"/><line x1="20" y1="90" x2="225" y2="90"/><line x1="20" y1="96" x2="225" y2="96"/><line x1="20" y1="102" x2="225" y2="102"/><line x1="20" y1="108" x2="225" y2="108"/><line x1="20" y1="114" x2="225" y2="114"/><line x1="20" y1="120" x2="225" y2="120"/><line x1="20" y1="132" x2="225" y2="132"/><line x1="20" y1="138" x2="225" y2="138"/><line x1="20" y1="143" x2="225" y2="143"/></g>
        <line x1="20" y1="149" x2="225" y2="149" stroke="#333" stroke-width=".6"/>
        <g font-size="4.5" class="t" fill="#444"><text x="8" y="38">20</text><text x="8" y="66">15</text><text x="8" y="94">10</text><text x="11" y="122">5</text><text x="11" y="150">0</text>
        <text x="19" y="157">0</text><text x="58" y="157">10</text><text x="99" y="157">20</text><text x="140" y="157">30</text><text x="181" y="157">40</text><text x="222" y="157">50</text></g>
      </svg></div>
      <h3>HISTOGRAM</h3>
      <p>Sed ut perspiciatis unde omnis iste natus error sit volup architecto beatae vitae dicta sunt explicabo.</p>
    </article>

    <article class="card">
      <div class="chart"><svg viewBox="0 0 240 182">
        <text x="50" y="52" font-size="5" font-weight="700" class="t">Population of Largest U.S. Cities</text>
        <g stroke="#ddd" stroke-width=".5"><line x1="112" y1="60" x2="112" y2="130"/><line x1="160" y1="60" x2="160" y2="130"/><line x1="208" y1="60" x2="208" y2="130"/></g>
        <line x1="64" y1="60" x2="64" y2="130" stroke="#333" stroke-width=".6"/>
        <g fill="var(--blue)"><rect x="64" y="65" width="104" height="3"/><rect x="64" y="78" width="48" height="3"/><rect x="64" y="92" width="34" height="3"/><rect x="64" y="105" width="27" height="3"/><rect x="64" y="118" width="19" height="3"/></g>
        <g fill="var(--red)"><rect x="64" y="68.5" width="101" height="3"/><rect x="64" y="81.5" width="47" height="3"/><rect x="64" y="95.5" width="37" height="3"/><rect x="64" y="108.5" width="25" height="3"/><rect x="64" y="121.5" width="19" height="3"/></g>
        <g font-size="4.3" class="t" fill="#333" text-anchor="end"><text x="61" y="70">New York City, NY</text><text x="61" y="83">Los Angeles, CA</text><text x="61" y="97">Chicago, IL</text><text x="61" y="110">Houston, TX</text><text x="61" y="123">Philadelphia, PA</text></g>
        <g font-size="4.3" class="t" fill="#333"><text x="62" y="137">0</text><text x="102" y="137">2,500,000</text><text x="150" y="137">5,000,000</text><text x="196" y="137">7,500,000</text><text x="99" y="145" font-style="italic">Total Population</text></g>
        <rect x="182" y="63" width="8" height="3" fill="var(--blue)"/><rect x="182" y="70" width="8" height="3" fill="var(--red)"/>
        <g font-size="4.3" class="t"><text x="192" y="66">2010 Population</text><text x="192" y="73">2000 Population</text></g>
      </svg></div>
      <h3>BAR CHARTS</h3>
      <p>Sed ut perspiciatis unde omnis iste natus error sit volup architecto beatae vitae dicta sunt explicabo.</p>
    </article>

    <article class="card">
      <div class="chart"><svg viewBox="0 0 240 182">
        <text x="25" y="30" font-size="5" font-weight="700" class="t">My Daily Activities</text>
        <path d="M95 100 L95 40 A60 60 0 0 1 110.6 157.9Z" fill="var(--blue)" stroke="#fff" stroke-width=".6"/>
        <path d="M95 100 L110.6 157.9 A60 60 0 0 1 79.7 158Z" fill="var(--red)" stroke="#fff" stroke-width=".6"/>
        <path d="M95 100 L79.7 158 A60 60 0 0 1 52.8 142.6Z" fill="var(--amber)" stroke="#fff" stroke-width=".6"/>
        <path d="M95 100 L52.8 142.6 A60 60 0 0 1 37.2 115.9Z" fill="var(--green)" stroke="#fff" stroke-width=".6"/>
        <path d="M95 100 L37.2 115.9 A60 60 0 0 1 95 40Z" fill="var(--purple)" stroke="#fff" stroke-width=".6"/>
        <g font-size="5" class="t" fill="#fff"><text x="134" y="97">45.8%</text><text x="89" y="152">8.3%</text><text x="63" y="143">8.3%</text><text x="44" y="124">8.3%</text><text x="52" y="73">29.2%</text></g>
        <g font-size="5" class="t"><circle cx="178" cy="41" r="2.3" fill="var(--blue)"/><text x="183" y="43">Work</text>
        <circle cx="178" cy="50" r="2.3" fill="var(--red)"/><text x="183" y="52">Eat</text>
        <circle cx="178" cy="59" r="2.3" fill="var(--amber)"/><text x="183" y="61">Commute</text>
        <circle cx="178" cy="68" r="2.3" fill="var(--green)"/><text x="183" y="70">Watch TV</text>
        <circle cx="178" cy="77" r="2.3" fill="var(--purple)"/><text x="183" y="79">Sleep</text></g>
      </svg></div>
      <h3>VISUALIZATION: PIE CHART</h3>
      <p>Sed ut perspiciatis unde omnis iste natus error sit volup architecto beatae vitae dicta sunt explicabo.</p>
    </article>

    <article class="card">
      <div class="chart"><svg viewBox="0 0 240 182">
        <text x="22" y="30" font-size="4.2" font-weight="700" class="t">Correlation between life expectancy, fertility rate and population of some world</text>
        <text x="22" y="35" font-size="4.2" font-weight="700" class="t">countries (2010)</text>
        <g stroke="#ddd" stroke-width=".5"><line x1="22" y1="44" x2="204" y2="44"/><line x1="22" y1="68" x2="204" y2="68"/><line x1="22" y1="92" x2="204" y2="92"/><line x1="22" y1="116" x2="204" y2="116"/><line x1="67" y1="44" x2="67" y2="140"/><line x1="113" y1="44" x2="113" y2="140"/><line x1="158" y1="44" x2="158" y2="140"/><line x1="204" y1="44" x2="204" y2="140"/></g>
        <line x1="22" y1="140" x2="204" y2="140" stroke="#333" stroke-width=".6"/>
        <g font-size="4.3" class="t" fill="#444"><text x="12" y="46">6.0</text><text x="12" y="70">4.5</text><text x="12" y="94">3.0</text><text x="12" y="118">1.5</text><text x="12" y="142">0.0</text>
        <text x="20" y="148">65</text><text x="65" y="148">70</text><text x="110" y="148">75</text><text x="156" y="148">80</text><text x="201" y="148">85</text><text x="96" y="163" font-style="italic">Life Expectancy</text></g>
        <g stroke="#fff" stroke-width=".5"><circle cx="52" cy="63" r="3.5" fill="var(--amber)"/><circle cx="92" cy="93" r="4.5" fill="var(--amber)"/><circle cx="88" cy="112" r="4.2" fill="var(--amber)"/><circle cx="58" cy="114" r="6" fill="var(--red)"/><circle cx="140" cy="106" r="8" fill="var(--blue)"/><circle cx="158" cy="106" r="4.5" fill="var(--red)"/><circle cx="157" cy="118" r="4.5" fill="var(--red)"/><circle cx="163" cy="111" r="3" fill="var(--blue)"/><circle cx="174" cy="91" r="2" fill="var(--amber)"/></g>
        <g font-size="4" class="t"><rect x="207" y="44" width="4" height="4" fill="var(--blue)"/><text x="213" y="48">N. America</text><rect x="207" y="51" width="4" height="4" fill="var(--red)"/><text x="213" y="55">Europe</text><rect x="207" y="58" width="4" height="4" fill="var(--amber)"/><text x="213" y="62">Middle East</text></g>
      </svg></div>
      <h3>VISUALIZATION: BUBBLE CHART</h3>
      <p>Sed ut perspiciatis unde omnis iste natus error sit volup architecto beatae vitae dicta sunt explicabo.</p>
    </article>

    <article class="card">
      <div class="chart"><svg viewBox="0 0 240 182">
        <rect x="8" y="34" width="224" height="3" fill="#bbb"/><text x="115" y="37" font-size="3.5" class="t" text-anchor="middle">Global</text>
        <rect x="160" y="30" width="72" height="2" fill="var(--green)"/><rect x="160" y="30" width="30" height="2" fill="var(--red)"/>
        <rect x="8" y="38" width="72" height="120" fill="#c3d6c1" stroke="#fff"/>
        <rect x="80" y="38" width="66" height="120" fill="#d99ca1" stroke="#fff"/>
        <rect x="146" y="38" width="86" height="67" fill="#c8d2c8" stroke="#fff"/>
        <rect x="146" y="105" width="86" height="53" fill="#b3d9ad" stroke="#fff"/>
        <g font-size="3.5" class="t" text-anchor="middle"><text x="44" y="99">Asia</text><text x="113" y="99">Europe</text><text x="189" y="72">America</text><text x="189" y="133">Africa</text></g>
      </svg></div>
      <h3>TREEMAPS</h3>
      <p>Sed ut perspiciatis unde omnis iste natus error sit volup architecto beatae vitae dicta sunt explicabo.</p>
    </article>

    <article class="card">
      <div class="chart"><svg viewBox="0 0 240 182">
        <text x="28" y="36" font-size="4.5" font-weight="700" class="t">Company Performance</text>
        <g stroke="#ddd" stroke-width=".5"><line x1="30" y1="44" x2="197" y2="44"/><line x1="30" y1="68" x2="197" y2="68"/><line x1="30" y1="92" x2="197" y2="92"/><line x1="30" y1="116" x2="197" y2="116"/></g>
        <path d="M30 140 L30 67 L86 46 L141 88 L197 58 L197 140Z" fill="var(--blue)" fill-opacity=".38" stroke="#3a6fe0" stroke-width=".8"/>
        <path d="M30 140 L30 108 L86 103 L141 49 L197 96 L197 140Z" fill="var(--red)" fill-opacity=".38" stroke="#e04b37" stroke-width=".8"/>
        <line x1="30" y1="140" x2="197" y2="140" stroke="#333" stroke-width=".6"/>
        <g font-size="4.3" class="t" fill="#444"><text x="16" y="46">1,200</text><text x="19" y="70">900</text><text x="19" y="94">600</text><text x="19" y="118">300</text><text x="25" y="142">0</text>
        <text x="25" y="147">2013</text><text x="81" y="147">2014</text><text x="136" y="147">2015</text><text x="192" y="147">2016</text><text x="107" y="158" font-style="italic">Year</text></g>
        <g font-size="4" class="t"><line x1="200" y1="45" x2="208" y2="45" stroke="#3a6fe0"/><text x="210" y="47">Sales</text><line x1="200" y1="51" x2="208" y2="51" stroke="#e04b37"/><text x="210" y="53">Expenses</text></g>
      </svg></div>
      <h3>VISUALIZATION: AREA CHART</h3>
      <p>Sed ut perspiciatis unde omnis iste natus error sit volup architecto beatae vitae dicta sunt explicabo.</p>
    </article>

    <article class="card">
      <div class="chart"><svg viewBox="0 0 240 182">
        <g fill="#bdbdbd" fill-opacity=".8">
          <path d="M12 38 C120 38 120 32 228 32 L228 46 C120 46 120 52 12 52Z"/>
          <path d="M12 54 C120 54 120 62 228 62 L228 90 C120 90 120 82 12 82Z"/>
          <path d="M12 84 C120 84 120 118 228 118 L228 130 C120 130 120 96 12 96Z"/>
          <path d="M12 97 C120 97 120 42 228 42 L228 56 C120 56 120 110 12 110Z"/>
          <path d="M12 112 C120 112 120 92 228 92 L228 116 C120 116 120 136 12 136Z"/>
          <path d="M12 137 C120 137 120 132 228 132 L228 152 C120 152 120 152 12 152Z"/>
        </g>
        <rect x="9" y="38" width="4" height="58" fill="#3b62d6"/><rect x="9" y="97" width="4" height="55" fill="#a23bb2"/>
        <rect x="227" y="32" width="4" height="28" fill="#d43b3b"/><rect x="227" y="62" width="4" height="54" fill="#f0b21a"/><rect x="227" y="118" width="4" height="34" fill="#2e9a3e"/>
        <g font-size="3.6" class="t"><text x="16" y="68">A</text><text x="16" y="124">B</text><text x="221" y="47">X</text><text x="221" y="90">Y</text><text x="221" y="136">Z</text></g>
      </svg></div>
      <h3>SANKEY DIAGRAM</h3>
      <p>Sed ut perspiciatis unde omnis iste natus error sit volup architecto beatae vitae dicta sunt explicabo.</p>
    </article>
  </main>

  <footer class="footer">© Copyright-2018 Reactly. All rights reserved.</footer>
</div>
</body>
</html>
```